Trendy eye catching business card for lawn mowing business

Verge Crew, a local community lawn mowing service, requires an eye catching trendy business card to drop into letterboxes.

We could simply throw something together from a Microsoft Word template, but we are wanting something more than this. Some other business’ images are attached for some inspiration.

We are requiring the card to have Verge Crew with our slogan, Call The Pellows. In addition, provide details with that we are a local, affordable lawn mowing service, and for other gardening matters to simply just ask!
Plus the relevant contact details, phone, email, social media.

Target Market(s)

Local community members who require assistance with their garden care

Industry/Entity Type

Gardening

Contact Information for Business Card

the name VERGE CREW is our logo
telephone logo 0493 218 067
email logo vergecrew@postbox-example.com
Instagram logo vergecrew
Facebook logo vergecrew.sth
Lawn Mowing Service
Local Affordable
edge trim, blow and clipping removal included.
Other gardening matters, just ask!

Font styles to use
Serif
Sans Serif
Decorative
Script

Colors
9bcb3c
ffffff

Requirements
Must have
• All the details listed in Business Card Details.
Make these words prominent:
Verge Crew
Lawn Mowing Service
Local
Affordable
Nice to have
• Our slogan ‘Call The Pellows’ incorporated.
Different colour background for front and reverse side
Greens, white and black colours
Subtle grass blades images incorporated
Should not have
• No images of lawnmowers.
No images of men/cartoons.
No using initials for Verge Crew

```html
<!DOCTYPE html>
<html lang="en">
<head>
<meta charset="utf-8">
<title>Verge Crew – Business Card</title>
<link rel="stylesheet" href="https://fonts.googleapis.com/css2?family=Archivo+Black&family=Quicksand:wght@500;600;700&display=swap">
<style>
  :root {
    --lawn-green: #9bcb3c;
    --white: #ffffff;
    --charcoal: #4a4a4a;
    --ink: #3a3a3a;
    --backdrop: #2a2a2a;
  }
  * { box-sizing: border-box; margin: 0; padding: 0; }
  html, body { width: 1200px; height: 900px; overflow: hidden; background: var(--backdrop); }
  .canvas {
    position: relative; width: 1200px; height: 900px;
    display: flex; flex-direction: column; align-items: center; justify-content: center; gap: 36px;
  }
  .card {
    position: relative; width: 720px; height: 410px; overflow: hidden;
    box-shadow: 0 10px 30px rgba(0,0,0,.45);
  }
  .brand-name {
    font-family: "Archivo Black", sans-serif; line-height: .9; letter-spacing: .5px;
  }
  .brand-slogan {
    font-family: "Quicksand", sans-serif; font-weight: 700; letter-spacing: 1.5px;
    text-transform: uppercase; font-size: 13px;
  }

  /* Front */
  .card-front { background: var(--lawn-green); color: var(--white); text-align: center; }
  .card-front .brand { padding-top: 44px; }
  .card-front .brand-name { font-size: 52px; color: var(--white); }
  .card-front .brand-slogan { color: var(--ink); margin-top: 6px; }
  .service-list { list-style: none; margin-top: 18px; }
  .service-list li {
    font-family: "Archivo Black", sans-serif; font-size: 24px; line-height: 1.1; color: var(--white);
    display: flex; justify-content: center; align-items: center; gap: 8px;
  }
  .chevron { width: 9px; height: 12px; fill: var(--ink); }
  .divider { width: 520px; height: 1px; background: var(--white); margin: 18px auto 12px; }
  .inclusions { font-family: "Quicksand", sans-serif; font-weight: 500; font-size: 17px; line-height: 1.3; }
  .inclusions .ask { text-transform: uppercase; }

  /* Back */
  .card-back { background: var(--white); }
  .card-back .swoosh { position: absolute; inset: 0; }
  .card-back .brand { position: absolute; left: 60px; top: 44px; }
  .card-back .brand-name { font-size: 50px; color: var(--lawn-green); }
  .card-back .brand-slogan { color: var(--ink); margin-top: 6px; }
  .contact { position: absolute; right: 36px; top: 196px; text-align: right; color: var(--white); font-family: "Quicksand", sans-serif; }
  .person-name { font-family: "Quicksand", sans-serif; font-weight: 700; font-size: 32px; line-height: 1.1; color: var(--lawn-green); letter-spacing: 1px; }
  .person-role { font-size: 18px; font-weight: 600; margin-bottom: 12px; }
  .contact-list { list-style: none; }
  .contact-list li {
    display: flex; justify-content: flex-end; align-items: center; gap: 12px;
    font-size: 18px; font-weight: 600; line-height: 1.5;
  }
  .contact-list li.gap-above { margin-top: 6px; }
  .contact-icon { width: 20px; height: 20px; stroke: var(--lawn-green); fill: none; stroke-width: 1.8; }
  .social-dot { width: 18px; height: 18px; margin: 0 1px; border-radius: 4px; background: var(--lawn-green); }
</style>
</head>
<body>
<main class="canvas">

  <section class="card card-front" aria-label="Card front">
    <div class="brand">
      <h1 class="brand-name">VERGE<br>CREW</h1>
      <p class="brand-slogan">Call The Pellows</p>
    </div>
    <ul class="service-list">
      <li><svg class="chevron" viewBox="0 0 9 12"><path d="M0 0h4l5 6-5 6H0l5-6z"/></svg>VERGE CREW<svg class="chevron" viewBox="0 0 9 12"><path d="M9 0H5L0 6l5 6h4L4 6z"/></svg></li>
      <li><svg class="chevron" viewBox="0 0 9 12"><path d="M0 0h4l5 6-5 6H0l5-6z"/></svg>LAWN MOWING SERVICE<svg class="chevron" viewBox="0 0 9 12"><path d="M9 0H5L0 6l5 6h4L4 6z"/></svg></li>
      <li><svg class="chevron" viewBox="0 0 9 12"><path d="M0 0h4l5 6-5 6H0l5-6z"/></svg>LOCAL<svg class="chevron" viewBox="0 0 9 12"><path d="M9 0H5L0 6l5 6h4L4 6z"/></svg></li>
      <li><svg class="chevron" viewBox="0 0 9 12"><path d="M0 0h4l5 6-5 6H0l5-6z"/></svg>AFFORDABLE<svg class="chevron" viewBox="0 0 9 12"><path d="M9 0H5L0 6l5 6h4L4 6z"/></svg></li>
    </ul>
    <div class="divider"></div>
    <p class="inclusions">Edge trim, blow and clipping removal included.<br>Other gardening matters, <span class="ask">just ask!</span></p>
  </section>

  <section class="card card-back" aria-label="Card back">
    <svg class="swoosh" viewBox="0 0 720 410" preserveAspectRatio="none" aria-hidden="true">
      <path d="M0 262 C120 170 330 148 720 166 L720 410 L0 410 Z" fill="#4a4a4a"/>
      <path d="M0 270 C120 177 330 155 720 172 L720 182 C420 160 220 172 160 260 C132 305 128 360 130 410 L0 410 Z" fill="#9bcb3c"/>
    </svg>
    <div class="brand">
      <h2 class="brand-name">VERGE<br>CREW</h2>
      <p class="brand-slogan">Call The Pellows</p>
    </div>
    <div class="contact">
      <p class="person-name">DALE MORROW</p>
      <p class="person-role">Director/ Owner</p>
      <ul class="contact-list">
        <li>0493 218 067
          <svg class="contact-icon" viewBox="0 0 24 24"><path d="M5 3h4l2 5-2.5 1.5a11 11 0 0 0 6 6L16 13l5 2v4a2 2 0 0 1-2 2A17 17 0 0 1 3 5a2 2 0 0 1 2-2z"/></svg></li>
        <li>vergecrew@postbox-example.com
          <svg class="contact-icon" viewBox="0 0 24 24"><rect x="3" y="5" width="18" height="14" rx="1"/><path d="M3 6l9 7 9-7"/></svg></li>
        <li class="gap-above">@vergecrew <span class="social-dot"></span></li>
        <li>vergecrew.sth <span class="social-dot"></span></li>
      </ul>
    </div>
  </section>

</main>
</body>
</html>
```